Website Design: Business to Business Coaching/Strategy

DO NOT CONTACT ME PRIVATELY. ANY PRIVATE CONTACT WILL BE IGNORED.

I need a website design for a business to business coaching service.

The website is for a company the specializes in coaching/training for other businesses. The business specializes in business development and human resource management.

Where appropriate, please include calls to action, e.g.: book a service & request a quote

CONTENT (SEEE ATTACHMENT)
5 Pages;
1. Home Page with overview of company/services -> Slide show at the top with tagline:

WE HELP MAKE STRATEGY HAPPEN BY

DELIVERING LONG-TERM PERFORMANCE IMPROVEMENTS

SO COMPANIES CAN

"BECOME THE CHANGE THEY WISH TO SEE."

2. Works - core services; coaching; leadership development, workshops
3. Expertise
a. capability: helping people to help themselves
b. company interventions: working in partnership; team facilitation; …
c. testimonials
4. About Us
5. Inquires
a. business capability development and funding
b. Register / enrol for an open programme or workshop
c. client feedback

The website below provides services that are similar to the services of my company: https://www.velmoria.co.uk

DESIGN
- Dark theme matching this style of website BUT a simpler more straightforward design: https://www.hadlowcrest.ac.uk/
Another theme that I like - Dark themed with a modern/easy design: https://quorbastyles.com/theme-demos/?demo=lumetra-dark

Target Market(s)

Small businesses

Industry/Entity Type

Executive training/business coaching

Number of Pages Required

5+ page

Colors

Designer to choose colors to be used in the design.

```html
<!DOCTYPE html>
<html lang="en">
<head>
<meta charset="utf-8">
<title>Velmoria – Strategy &amp; Coaching</title>
<link href="https://fonts.googleapis.com/css2?family=Oswald:wght@300;400;500&family=Poppins:wght@300;400&family=Montserrat:ital,wght@1,400&display=swap" rel="stylesheet">
<style>
:root{
  --black:#000;
  --panel:#141414;
  --red:#9a0000;
  --red-line:#c40000;
  --white:#fff;
  --body:#a3a3a3;
  --muted:#cfcfcf;
}
*{margin:0;padding:0;box-sizing:border-box}
html,body{width:1200px;height:4938px;overflow:hidden;background:var(--black)}
body{position:relative;font-family:"Poppins",sans-serif;color:var(--white)}
.abs{position:absolute}
.hero{left:0;top:0;width:1200px;height:778px;background:linear-gradient(160deg,#3c3c3c 0%,#2a2a2a 35%,#1d1d1d 70%,#262626 100%)}
.brand{left:88px;top:54px;width:409px;height:99px;background:var(--red);display:flex;align-items:center;justify-content:center;font-family:"Poppins",sans-serif;font-weight:400;font-size:64px;letter-spacing:10px;color:var(--white)}
.nav{left:497px;top:54px;width:615px;height:99px;background:var(--black)}
.nav a{position:absolute;top:40px;font-family:"Oswald",sans-serif;font-weight:500;font-size:16px;color:var(--white);text-decoration:none;letter-spacing:.5px}
.nav a.current{color:#9a9a9a}
.hero-frame{left:211px;top:312px;width:780px;height:301px;border:2px solid var(--red-line);border-top:none}
.hero-frame::before,.hero-frame::after{content:"";position:absolute;top:0;height:2px;width:100px;background:var(--red-line)}
.hero-frame::before{left:0}.hero-frame::after{right:0}
.hero-title{left:211px;top:272px;width:780px;text-align:center;font-family:"Oswald",sans-serif;font-weight:300;font-size:58px;line-height:69px;color:var(--white)}
.hero-quote{left:211px;top:500px;width:780px;text-align:center;font-family:"Oswald",sans-serif;font-weight:500;font-size:40px}
.band{left:0;width:874px;background:var(--panel)}
.photo{}
h2.title{position:absolute;font-family:"Oswald",sans-serif;font-weight:500;font-size:40px;line-height:48px;color:var(--white)}
p.copy{position:absolute;font-size:18px;line-height:27.5px;font-weight:300;color:var(--body)}
.about{left:0;top:3939px;width:1066px;height:441px;background:var(--red)}
.about h2{position:absolute;left:0;top:98px;width:1150px;text-align:center;font-family:"Oswald",sans-serif;font-weight:500;font-size:44px}
.about p{position:absolute;left:0;top:184px;width:1200px;text-align:center;font-family:"Montserrat",sans-serif;font-style:italic;font-size:26px;line-height:34px}
.foot-head{font-size:18px;color:var(--white)}
.foot-small{font-size:12px;line-height:19px;color:var(--muted)}
.btn{left:454px;width:190px;height:49px;border:2px solid var(--red-line);display:flex;align-items:center;justify-content:center;font-size:18px;color:var(--muted)}
.rule{left:0;top:4758px;width:1200px;height:1px;background:#1c1c1c}
.foot-nav a{position:absolute;top:4818px;font-size:13px;color:var(--muted);text-decoration:none}
.legal span{position:absolute;top:4862px;font-size:12px;color:var(--muted)}
.social{top:4807px;width:36px;height:36px;border:2px solid #d8d8d8;border-radius:50%}
</style>
</head>
<body>

<header>
  <div class="abs hero" role="img" aria-label="Dimmed photo of a team working together around a meeting table"></div>
  <div class="abs brand">VELMORIA</div>
  <nav class="abs nav">
    <a class="current" style="left:76px">HOME</a>
    <a style="left:174px">WORKS</a>
    <a style="left:283px">EXPERTISE</a>
    <a style="left:410px">ABOUT US</a>
    <a style="left:527px">INQUIRES</a>
  </nav>
  <div class="abs hero-frame"></div>
  <h1 class="abs hero-title">WE HELP MAKE STRATEGY<br>HAPPEN BY DELIVERING<br>LONG-TERM PERFORMANCE</h1>
  <p class="abs hero-quote">"BECOME THE CHANGE THEY WISH TO SEE."</p>
</header>

<main>
  <section>
    <div class="abs band" style="top:778px;height:667px"></div>
    <h2 class="title" style="left:130px;top:928px">LEADERSHIP &amp; CAPABILITY</h2>
    <p class="copy" style="left:130px;top:1010px;width:390px">There is a pressing need for leadership to be distributed across organisations in support of constant innovation and change.&nbsp; For businesses that believe there is a benefit in investing in their core resource – people, we can help you gain a clear return on investment, improve profitability, build your leadership capacity and contribute to creating a high-performing organisation.</p>
    <div class="abs" style="left:569px;top:891px;width:583px;height:422px;background:linear-gradient(180deg,#8a8a8c,#56575a)" role="img" aria-label="Photo of wooden figures linked to one red figure in the centre"></div>
  </section>

  <section>
    <div class="abs" style="left:130px;top:1499px;width:506px;height:456px;background:linear-gradient(135deg,#d9dde2,#8da4be 60%,#4b6f9e)" role="img" aria-label="Photo of a hand with a pen reviewing printed charts"></div>
    <h2 class="title" style="left:684px;top:1558px">ASSESSMENT &amp; ANALYSIS</h2>
    <p class="copy" style="left:686px;top:1631px;width:400px">We engage key stakeholders to identify issues, clarify direction and to have conversations about those areas that really matter.&nbsp; We help clients to commit to action, implement new business strategies, plan for the future and achieve business&nbsp; growth. Our personalised coaching enables us to put an objective lens on the goals you wish to achieve.</p>
  </section>

  <section>
    <div class="abs band" style="top:2034px;height:667px"></div>
    <h2 class="title" style="left:130px;top:2174px">PEOPLE &amp; ENGAGEMENT</h2>
    <p class="copy" style="left:130px;top:2248px;width:532px">It's all about people; that is, the right people. Having leaders with an ability to facilitate the fulfilment of your company's purpose through your people provides potential for it to become a great organisation. Dealing with change is dealing with peoples emotions.&nbsp; We are interested in improvement, not change.&nbsp; Specifically, we are keen on developing companies and leaders who want to create a great organisation and are willing to lead a process that engages stakeholders in its quest for continuous improvement and long-term viability</p>
    <div class="abs" style="left:707px;top:2160px;width:493px;height:420px;background:linear-gradient(135deg,#e6e1d8,#a89a88 55%,#5a4c40)" role="img" aria-label="Photo of a speaker addressing a group in a bright room"></div>
  </section>

  <section>
    <div class="abs" style="left:130px;top:2818px;width:506px;height:456px;background:linear-gradient(135deg,#e4e4e4,#8c8c90 50%,#1f2533)" role="img" aria-label="Photo of two colleagues in suits reviewing a tablet and documents"></div>
    <h2 class="title" style="left:680px;top:2827px">INVESTIGATE &amp; GUIDE</h2>
    <p class="copy" style="left:686px;top:2902px;width:406px">Success in bussiness hinges on strategic agility as well as an ability to highlight and execute actions leading to measurable improvements.&nbsp; To help businesses to do this we will support, guide and partner with clients to assess, plan for and strengthen their capability through the design of strategies to overcome barriers and produce measurable impact.&nbsp; Our experience in consultancy and company intervention will provide an objective focus to uncover unknown factors and develop an actionable plan for you to execute</p>
  </section>

  <section>
    <h2 class="title" style="left:134px;top:3506px">A PERSONALISED<br>APPROACH</h2>
    <p class="copy" style="left:134px;top:3627px;width:320px">Working in partnership we wil learn about your business and your challenges for the purpose of designing a programme appropriate to your situation</p>
    <div class="abs" style="left:479px;top:3426px;width:721px;height:385px;background:linear-gradient(135deg,#4a4a4a,#8a7560 50%,#3a3a3a)" role="img" aria-label="Photo of hands stacking wooden blocks labelled with planning words"></div>
  </section>

  <section class="abs about">
    <h2>ABOUT COMPANY</h2>
    <p>Lumenfold Enterprise specialise in helping<br>clients make strategy happen by delivering<br>long-term performance improvements so they<br>can "become the change they wish to see."</p>
  </section>
</main>

<footer>
  <p class="abs foot-head" style="left:130px;top:4455px">CONTACT US</p>
  <p class="abs foot-small" style="left:130px;top:4500px">Tel: +44 (0)20 7946 0381<br>Email: info@velmoria.co.uk</p>
  <p class="abs foot-small" style="left:130px;top:4550px"><span style="font-size:14px">Velmoria UK</span><br>Velmoria Partners LLP<br>2nd Floor, Calder House (CHBP)<br>12-18 Fenwick Row<br>London<br>E2 7QT<br>United Kingdom</p>
  <div class="abs btn" style="top:4463px">OUR COACHES</div>
  <div class="abs btn" style="top:4549px">CONTACT US</div>
  <p class="abs foot-head" style="left:760px;top:4455px;width:300px;text-align:center">Velmoria Offices Worldwide</p>
  <div class="abs" style="left:757px;top:4514px;width:307px;height:163px;background:#8a8a8a;border-radius:40px" role="img" aria-label="Grey world map showing office locations"></div>
  <div class="abs rule"></div>
  <nav class="foot-nav">
    <a style="left:130px">HOME</a>
    <a style="left:207px">OUR COACHES</a>
    <a style="left:341px">WHAT WE DO</a>
    <a style="left:466px">PRIVACY POLICY</a>
    <a style="left:610px">CONTACT US</a>
  </nav>
  <div class="legal">
    <span style="left:130px">© 2022&nbsp; All Rights Reserved.</span>
    <span style="left:323px">User Agreement</span>
    <span style="left:466px">Privacy Policy</span>
    <span style="left:591px">Cookie Policy</span>
  </div>
  <div class="abs social" style="left:898px" aria-label="Social link"></div>
  <div class="abs social" style="left:942px" aria-label="Social link"></div>
  <div class="abs social" style="left:986px" aria-label="Social link"></div>
  <div class="abs social" style="left:1031px" aria-label="Social link"></div>
</footer>

</body>
</html>
```